Invitation For Service Management Event

We need an invitation for clients to an event on the platform service Management. This has to be appealing and needs to be "tech" inspired. it is important that the design of the invitation is as clean as possible. I attached some images so that you understand the kind of enviorment we want to portray in the invitation.
- I also attached our company logo to the brief under the file Brelunox Transparent. The logo has to be in the invitation.

```html
<!DOCTYPE html>
<html lang="en">
<head>
<meta charset="utf-8">
<title>Platform Service Management – Invitation</title>
<link href="https://fonts.googleapis.com/css2?family=Montserrat:wght@400;500;600;700&display=swap" rel="stylesheet">
<style>
  :root {
    --red: #e0322c;
    --red-deep: #b3130f;
    --ink: #1b1b1d;
    --night: #0b0b0c;
    --paper: #f5f7fa;
    --gold: #e9a23b;
    --white: #ffffff;
  }
  * { margin: 0; padding: 0; box-sizing: border-box; }
  html, body { width: 857px; height: 1200px; overflow: hidden; }
  body { font-family: 'Montserrat', Arial, sans-serif; color: var(--ink); background: var(--paper); }
  .invitation { position: relative; width: 857px; height: 1200px; background: var(--paper); }

  .hero { position: absolute; left: 0; top: 0; width: 857px; height: 595px; overflow: hidden; }
  .hero-backdrop {
    position: absolute; inset: 0;
    background:
      radial-gradient(ellipse at 50% 55%, rgba(190,30,25,0.55) 0%, rgba(90,10,8,0.35) 40%, rgba(10,10,10,0) 75%),
      linear-gradient(180deg, #1a0c0b 0%, #2a0d0b 45%, #130909 100%);
  }
  .hero-emblem { position: absolute; left: 0; top: 0; }
  .hero-text {
    position: absolute; left: 228px; top: 180px; width: 400px;
    text-align: center; color: var(--white);
  }
  .hero-kicker { font-size: 18px; font-weight: 500; letter-spacing: 0.2px; }
  .hero-title {
    margin-top: 24px; color: var(--red);
    font-size: 38px; font-weight: 500; line-height: 44px; letter-spacing: 0.3px;
  }

  .details { position: absolute; left: 0; top: 595px; width: 857px; text-align: center; }
  .brand { margin-top: 70px; display: inline-flex; align-items: center; gap: 14px; }
  .brand-mark { width: 54px; height: 54px; border-radius: 50%; background: var(--red); }
  .brand-text { text-align: left; }
  .brand-name { font-size: 34px; font-weight: 700; color: var(--ink); line-height: 36px; letter-spacing: 0.5px; }
  .brand-tagline { font-size: 13px; font-weight: 600; color: var(--red); letter-spacing: 0.4px; }

  .event-when { margin-top: 38px; font-size: 27px; font-weight: 700; line-height: 36px; }
  .event-where { margin-top: 116px; font-size: 16px; font-weight: 400; line-height: 26px; }
  .rsvp { margin-top: 70px; font-size: 16px; line-height: 26px; }
  .rsvp-label { font-weight: 700; font-size: 17px; }

  .footer-band { position: absolute; left: 0; bottom: 0; width: 857px; height: 12px; background: var(--red); }
</style>
</head>
<body>
<div class="invitation">
  <section class="hero">
    <div class="hero-backdrop" role="img" aria-label="Dark red technology backdrop with hexagon grid and glowing circuit lines"></div>
    <svg class="hero-emblem" width="857" height="595" viewBox="0 0 857 595" aria-hidden="true">
      <circle cx="428" cy="321" r="180" fill="var(--night)"/>
      <circle cx="428" cy="321" r="162" fill="none" stroke="var(--gold)" stroke-width="1.5" opacity="0.8"/>
      <path d="M245 254 A195 195 0 0 0 577 446" fill="none" stroke="var(--red)" stroke-width="14"/>
    </svg>
    <div class="hero-text">
      <p class="hero-kicker">Come and join us</p>
      <h1 class="hero-title">PLATFORM<br>SERVICE<br>MANAGEMENT</h1>
    </div>
  </section>

  <section class="details">
    <div class="brand">
      <span class="brand-mark"></span>
      <div class="brand-text">
        <div class="brand-name">BRELUNOX</div>
        <div class="brand-tagline">IT CONSULTING AND SERVICES</div>
      </div>
    </div>
    <p class="event-when">1 - 5 December 2020<br>1pm - 3pm</p>
    <p class="event-where">48 Harbor Lane<br>Fairview, Northbay</p>
    <div class="rsvp">
      <p class="rsvp-label">RSVP</p>
      <p>By November 15th at<br>0198-7654-3210 or<br>www.brelunox.com/RSVP</p>
    </div>
  </section>

  <div class="footer-band"></div>
</div>
</body>
</html>
```